Paper and board wholesaler needs business card design for managers

We need a business card design that incorporates bordo red, white and/ or grey colors. The business card has to have our "KRITEX" logo and our partners paper group logo that we are part of - "VORMA group". Both of the logos should be applied to the business card according to the guidelines for the usage of the logo that have been added in the uploaded files.
The letters (information on the card) should be easily readable, so no "shiny" or "glossy" text.
Besides the two logos, the business card needs to contain information for the respective person:
1) Name, Surname,
2) Job position (e.g. "sales represantative"),
3) E-mail,
4) Phone number,
5) text: "Drukātavas Sēta (KRITEX)" LTD
6) our office address "Riga, Kalnupes street 42".
(also could have) 7) our homepage address "www.kritex.lv"
Holiday season, so have a lot of tasks to take care of and not as much time to check ArtHive as often.
1) Name, Surname, 2) Job position (e.g. "sales represantative"), 3) E-mail, 4) Phone number, 5) text: "Drukātavas Sēta (KRITEX)" LTD 6) our office address "Riga, Kalnupes street 42". (also could have) 7) our homepage address "www.kritex.lv"
- Josefin Sans

```html
<!DOCTYPE html>
<html lang="lv">
<head>
<meta charset="utf-8">
<title>KRITEX business card</title>
<link href="https://fonts.googleapis.com/css2?family=Poppins:wght@400;500;600&display=swap" rel="stylesheet">
<style>
  :root {
    --bordo: #822f35;
    --bordo-deep: #5a1d22;
    --white: #ffffff;
    --ink: #1e1e1e;
    --partner-green: #0f7f5e;
    --backdrop: #c4c4c4;
  }
  * { margin: 0; padding: 0; box-sizing: border-box; }
  html, body {
    width: 1093px; height: 1200px; overflow: hidden;
    background: var(--backdrop);
    font-family: "Poppins", sans-serif;
  }
  .card {
    position: absolute; left: 264px;
    width: 580px; height: 357px;
    overflow: hidden;
  }
  .card--front { top: 226px; background: var(--white); }
  .card--back { top: 620px; background: var(--bordo); }

  .front__band {
    position: absolute; left: 0; top: 0;
    width: 100%; height: 129px; background: var(--bordo);
  }
  .wordmark {
    position: absolute;
    font-weight: 500;
    line-height: 1; white-space: nowrap;
  }
  .card--front .wordmark {
    left: 26px; top: 48px; font-size: 28px; letter-spacing: 22px; color: var(--white);
  }
  .front__logo-panel {
    position: absolute; left: 356px; top: 35px;
    width: 143px; height: 180px; background: var(--white);
  }
  .front__logo-square {
    position: absolute; left: 373px; top: 70px;
    width: 110px; height: 110px; background: var(--bordo);
  }
  .person { position: absolute; left: 27px; top: 155px; }
  .person__name {
    font-size: 24px; font-weight: 500; color: var(--bordo);
    line-height: 1.1; letter-spacing: 0.2px;
  }
  .person__role { font-size: 17px; color: var(--ink); line-height: 1.15; }

  .contacts { position: absolute; left: 27px; top: 210px; list-style: none; }
  .contacts li {
    display: flex; align-items: center; gap: 7px;
    font-size: 17px; color: var(--ink); line-height: 21px;
  }
  .contacts svg { width: 15px; height: 15px; flex: none; }

  .company {
    position: absolute; left: 27px; top: 289px;
    font-size: 17.5px; line-height: 21px; color: var(--ink);
  }
  .partner {
    position: absolute; left: 334px; top: 295px;
    display: flex; align-items: center; gap: 10px;
    color: var(--partner-green); font-weight: 600; font-size: 22px; line-height: 1;
  }
  .partner__dot {
    width: 38px; height: 38px; border-radius: 50%; background: var(--partner-green);
  }

  .back__square {
    position: absolute; left: 249px; top: 88px;
    width: 82px; height: 82px; background: var(--bordo-deep);
  }
  .card--back .wordmark {
    left: 0; top: 236px; width: 100%; text-align: center;
    font-size: 32px; letter-spacing: 30px; padding-left: 30px;
    color: var(--bordo-deep);
  }
</style>
</head>
<body>
  <section class="card card--front" aria-label="Business card, front">
    <div class="front__band"></div>
    <div class="wordmark">KRITEX</div>
    <div class="front__logo-panel"></div>
    <div class="front__logo-square"></div>

    <div class="person">
      <p class="person__name">JONATHAN SMITH</p>
      <p class="person__role">Managing Director</p>
    </div>

    <ul class="contacts">
      <li>
        <svg viewBox="0 0 16 16" aria-hidden="true"><path fill="#822f35" d="M3.5 1.5l2.3 2.6-1.3 1.6c.8 1.9 2.1 3.3 4 4.2l1.6-1.3 2.6 2.3-1.5 2.4C6.4 13 2.9 9.5 1.2 4.7z"/><path fill="none" stroke="#822f35" stroke-width="1.3" d="M9 3a4 4 0 0 1 4 4M9 .8a6.2 6.2 0 0 1 6.2 6.2"/></svg>
        067-480 215 903
      </li>
      <li>
        <svg viewBox="0 0 16 16" aria-hidden="true"><rect x="0.5" y="3" width="15" height="10" fill="#822f35"/><path d="M1 3.5l7 5 7-5M1 12.5l5-4.5M15 12.5l-5-4.5" fill="none" stroke="#fff" stroke-width="1"/></svg>
        office@kritex.lv
      </li>
      <li>
        <svg viewBox="0 0 16 16" aria-hidden="true"><g fill="none" stroke="#822f35" stroke-width="1.3"><circle cx="8" cy="8" r="7"/><ellipse cx="8" cy="8" rx="3" ry="7"/><path d="M1 8h14M2.2 4.5h11.6M2.2 11.5h11.6"/></g></svg>
        www.kritex.lv
      </li>
    </ul>

    <p class="company">Drukātavas Sēta (KRITEX) LTD<br>Riga, Kalnupes street 42</p>

    <div class="partner">
      <span class="partner__dot"></span>
      <span class="partner__name">VORMA group</span>
    </div>
  </section>

  <section class="card card--back" aria-label="Business card, back">
    <div class="back__square"></div>
    <div class="wordmark">KRITEX</div>
  </section>
</body>
</html>
```